We need a flyer design for a new fencing business. We do ferrowane fencing instalations and pride our company on Reliabilty, Dependabilty and genuine quality. Because it's not just a fence... It's your fence. Our company offers customer free quotes. Things that would need to be on the flyer;

*Company Name - Valley Copperpath Fencing
*Company email - copperpathfencing@quillmail.net
*Company Phone number - 0455 912 307

*Ferrowane fence specialist
*Free quotes

```html
<!DOCTYPE html>
<html lang="en">
<head>
<meta charset="utf-8">
<title>Valley Copperpath Fencing – Flyer</title>
<link rel="stylesheet" href="https://fonts.googleapis.com/css2?family=Abril+Fatface&family=Barlow+Semi+Condensed:wght@400;500;700;800&display=swap">
<style>
:root{
  --navy:#1d2a6e;
  --red:#8e1b1f;
  --white:#ffffff;
  --ink:#1d2a6e;
  --sw-red:#8b1a1a;--sw-peach:#f6d2ba;--sw-tan:#d9c48e;--sw-blush:#ebc4ab;
  --sw-mauve:#8a6e7e;--sw-forest:#3d5d4b;--sw-sage:#7e9e7e;--sw-mint:#68c27e;
  --sw-green:#33b068;--sw-leaf:#1e9a46;--sw-moss:#5a8a6a;--sw-blue:#17506e;
  --sw-stone:#b1a794;--sw-olive:#5f5a4a;
}
*{margin:0;padding:0;box-sizing:border-box}
html,body{width:849px;height:1200px;overflow:hidden;background:var(--white)}
.flyer{position:relative;width:849px;height:1200px;background:var(--white);font-family:"Barlow Semi Condensed",Arial,sans-serif;color:var(--ink)}
.swatches{position:absolute;top:0;width:65px;height:1200px;display:flex;flex-direction:column}
.swatches span{flex:1;border-bottom:2px solid #fff}
.swatches--left{left:0}
.swatches--right{right:0}
.brand{position:absolute;left:94px;top:0;width:663px;height:245px;font-family:"Abril Fatface",Georgia,serif;font-weight:400;color:var(--navy)}
.brand span{position:absolute;left:0;width:100%;white-space:nowrap}
.brand__main{top:22px;text-align:center;font-size:140px;line-height:128px;letter-spacing:8px}
.brand__sub{top:150px;text-align:right;font-size:50px;line-height:48px;letter-spacing:2px}
.brand__last{top:194px;text-align:left;font-size:48px;line-height:46px;letter-spacing:3px}
.tagline{position:absolute;left:94px;top:244px;width:663px;font-size:28px;line-height:36px;font-weight:500;color:var(--navy);white-space:nowrap}
.tagline strong{color:var(--red);font-weight:800;font-size:34px}
.photo{position:absolute}
.photo--a{left:94px;top:302px;width:182px;height:165px;background:linear-gradient(160deg,#8fa27c 0%,#ece3c6 55%,#d8cca6 100%)}
.photo--b{left:282px;top:302px;width:237px;height:165px;background:linear-gradient(180deg,#c9a07f 0%,#a82433 30%,#8c1726 80%,#5d6b3a 100%)}
.photo--c{left:525px;top:302px;width:230px;height:165px;background:linear-gradient(180deg,#b59b86 0%,#56585a 35%,#e7e0cf 60%,#59625a 100%)}
.photo--d{left:94px;top:476px;width:661px;height:203px;background:linear-gradient(180deg,#c4d6e4 0%,#e8ecdf 25%,#ebe7cf 70%,#5e8e3c 100%)}
.banner{position:absolute;left:94px;top:694px;width:663px;height:75px;background:linear-gradient(90deg,var(--navy) 0%,#3b2560 55%,var(--red) 100%);display:flex;align-items:center;color:var(--white);border-top:3px solid #fff;outline:2px solid #d8d8e6}
.banner__name{font-size:46px;font-weight:800;padding-left:16px}
.banner__word{font-size:40px;font-weight:500;padding:0 8px 0 12px;border-right:2px solid #fff;line-height:44px}
.banner__role{font-size:44px;font-weight:800;padding-left:10px}
.values{position:absolute;left:94px;top:784px;width:663px;font-size:40px;line-height:50px;display:flex;justify-content:center;gap:10px;color:var(--navy);white-space:nowrap}
.values .sep{border-left:2px solid var(--navy)}
.values strong{color:var(--red);font-weight:800}
.promise{position:absolute;left:94px;top:849px;width:663px;height:80px;display:flex;align-items:center;justify-content:space-between;font-size:48px;font-weight:500;color:var(--navy);white-space:nowrap}
.promise__badge{display:inline-flex;align-items:center;justify-content:center;width:200px;height:80px;border-radius:50%;background:linear-gradient(120deg,var(--navy),#46245e 55%,var(--red));color:var(--white);font-weight:700;font-size:46px}
.offer{position:absolute;left:94px;top:944px;width:663px;display:flex;justify-content:center;align-items:center;font-family:"Abril Fatface",Georgia,serif;font-size:64px;letter-spacing:8px;line-height:64px;white-space:nowrap}
.offer__free{color:var(--red);padding-right:10px;border-right:2px solid var(--navy)}
.offer__quotes{color:var(--navy);padding-left:10px}
.contact{position:absolute;left:94px;width:663px;white-space:nowrap;color:var(--navy)}
.contact--phone{top:1018px;font-size:40px;line-height:80px;font-weight:500}
.contact--phone strong{color:var(--red);font-size:76px;font-weight:800;letter-spacing:2px;vertical-align:-4px}
.contact--email{top:1100px;font-size:34px;line-height:44px;font-weight:500}
.contact--email strong{color:var(--red);font-weight:800;font-size:36px}
</style>
</head>
<body>
<main class="flyer">
  <div class="swatches swatches--left" aria-hidden="true">
    <span style="background:var(--sw-red)"></span><span style="background:var(--sw-peach)"></span><span style="background:var(--sw-tan)"></span><span style="background:var(--sw-blush)"></span><span style="background:var(--sw-mauve)"></span><span style="background:var(--sw-forest)"></span><span style="background:var(--sw-sage)"></span><span style="background:var(--sw-mint)"></span><span style="background:var(--sw-green)"></span><span style="background:var(--sw-leaf)"></span><span style="background:var(--sw-moss)"></span><span style="background:var(--sw-blue)"></span><span style="background:var(--sw-stone)"></span><span style="background:var(--sw-olive)"></span>
  </div>
  <div class="swatches swatches--right" aria-hidden="true">
    <span style="background:var(--sw-olive)"></span><span style="background:var(--sw-stone)"></span><span style="background:var(--sw-blue)"></span><span style="background:var(--sw-moss)"></span><span style="background:var(--sw-leaf)"></span><span style="background:var(--sw-green)"></span><span style="background:var(--sw-mint)"></span><span style="background:var(--sw-sage)"></span><span style="background:var(--sw-forest)"></span><span style="background:var(--sw-mauve)"></span><span style="background:var(--sw-blush)"></span><span style="background:var(--sw-tan)"></span><span style="background:var(--sw-peach)"></span><span style="background:var(--sw-red)"></span>
  </div>

  <h1 class="brand">
    <span class="brand__main">Valley</span>
    <span class="brand__sub">Copperpath</span>
    <span class="brand__last">Fencing</span>
  </h1>

  <p class="tagline">Because it’s not just a fence... <strong>It’s your fence</strong></p>

  <div class="photo photo--a" role="img" aria-label="Photo of a cream steel fence beside a brick house and garden"></div>
  <div class="photo photo--b" role="img" aria-label="Photo of a red steel fence with lattice top in a backyard"></div>
  <div class="photo photo--c" role="img" aria-label="Photo of a grey steel fence with decorative top in front of a brick home"></div>
  <div class="photo photo--d" role="img" aria-label="Photo of a long cream steel fence with lattice top against the sky and hedges"></div>

  <div class="banner">
    <span class="banner__name">Ferrowane</span>
    <span class="banner__word">fence</span>
    <span class="banner__role">specialist</span>
  </div>

  <p class="values"><span>Reliable</span><span class="sep"></span><strong>Professional</strong><span class="sep"></span><span>Dependable</span></p>

  <p class="promise"><span>Genuine</span><span class="promise__badge">Quality</span><span>Guaranteed</span></p>

  <p class="offer"><span class="offer__free">FREE</span><span class="offer__quotes">QUOTES</span></p>

  <p class="contact contact--phone">Telephone: <strong>0455 912 307</strong></p>
  <p class="contact contact--email">email: <strong>copperpathfencing@quillmail.net</strong></p>
</main>
</body>
</html>
```